Retractable banner.
Health Check For Pets
Check for Ear Mites
Skin Health
Fleas & Ticks

A space SERVE BY <NAME OF CLINIC>

Ideally contain pictures of cats and dogs

```html
<!DOCTYPE html>
<html lang="en">
<head>
<meta charset="utf-8">
<title>Health Check For Pets – Roll-up Banner</title>
<link rel="stylesheet" href="https://fonts.googleapis.com/css2?family=Montserrat:wght@700;800;900&display=swap">
<style>
  :root {
    --backdrop: #2b3038;
    --paper: #ffffff;
    --brand-red: #c3161f;
    --brand-red-deep: #a9121b;
    --ink: #111111;
    --footer-bg: #efefef;
    --footer-ink: #555555;
    --ring: #4a4f55;
    --icon-bg: #f1f1f1;
    --cat-tone: #8c8f96;
    --dog-tone: #eedcbc;
  }
  * { margin: 0; padding: 0; box-sizing: border-box; }
  html, body {
    width: 768px; height: 1200px; overflow: hidden;
    background: var(--backdrop);
    font-family: "Montserrat", sans-serif;
  }
  .banner {
    position: absolute; left: 134px; top: 25px;
    width: 500px; height: 1150px;
    background: var(--paper);
    overflow: hidden;
  }
  .pet-photo { position: absolute; }
  .pet-photo--cat {
    left: 41px; top: 88px; width: 198px; height: 259px;
    border-radius: 90px 90px 14px 14px;
    background: linear-gradient(180deg, #a3a6ac 0%, var(--cat-tone) 60%, #767980 100%);
  }
  .pet-photo--dog {
    left: 239px; top: 5px; width: 231px; height: 374px;
    border-radius: 110px 110px 18px 18px;
    background: linear-gradient(180deg, #f5e6cb 0%, var(--dog-tone) 55%, #e2cca6 100%);
  }
  .headline {
    position: absolute; left: 0; width: 100%;
    text-align: center; color: var(--brand-red);
    font-weight: 900; line-height: 1;
  }
  .headline--health { top: 368px; font-size: 62px; letter-spacing: 1px; }
  .headline--check { top: 425px; font-size: 106px; letter-spacing: -2px; }
  .headline--pets { top: 514px; font-size: 52px; }
  .tick { position: absolute; left: 370px; top: 402px; width: 84px; height: 84px; }
  .checklist {
    position: absolute; left: 0; top: 570px; width: 100%; height: 473px;
    background: linear-gradient(135deg, var(--brand-red) 0%, var(--brand-red) 50%, var(--brand-red-deep) 50.2%, var(--brand-red-deep) 100%);
  }
  .checklist__rail {
    position: absolute; left: 131px; top: 80px; width: 6px; height: 310px;
    background: var(--icon-bg);
  }
  .check-item { position: absolute; left: 0; width: 100%; height: 144px; }
  .check-item--mites { top: 10px; }
  .check-item--skin { top: 166px; }
  .check-item--fleas { top: 318px; }
  .check-item__icon {
    position: absolute; left: 62px; top: 0;
    width: 144px; height: 144px; border-radius: 50%;
    background: var(--icon-bg);
    border: 4px solid var(--ring);
  }
  .check-item__label {
    position: absolute; left: 224px; top: 22px;
    color: var(--paper); font-weight: 900;
    font-size: 46px; line-height: 1;
  }
  .footer {
    position: absolute; left: 0; top: 1043px; width: 100%; height: 107px;
    background: var(--footer-bg); text-align: center;
  }
  .footer__label {
    position: absolute; left: 35px; right: 35px; top: 25px;
    display: flex; align-items: center; gap: 8px;
    color: var(--footer-ink); font-weight: 800; font-size: 16px; letter-spacing: .5px;
  }
  .footer__label::before, .footer__label::after {
    content: ""; flex: 1; height: 2px; background: var(--footer-ink);
  }
  .footer__clinic {
    position: absolute; left: 0; width: 100%; top: 48px;
    color: var(--footer-ink); font-weight: 800; font-size: 33px;
  }
</style>
</head>
<body>
  <main class="banner">
    <div class="pet-photo pet-photo--cat" role="img" aria-label="Photo of a grey cat peeking over the edge with paws resting down"></div>
    <div class="pet-photo pet-photo--dog" role="img" aria-label="Photo of a golden retriever puppy peeking over the edge with paws resting down"></div>

    <h1>
      <span class="headline headline--health">HEALTH</span>
      <span class="headline headline--check">CHECK</span>
      <span class="headline headline--pets">FOR PETS</span>
    </h1>
    <svg class="tick" viewBox="0 0 84 84" aria-hidden="true">
      <path d="M6 52 L30 74 L82 8" fill="none" stroke="var(--brand-red)" stroke-width="12" stroke-linejoin="miter" transform="translate(3 4)"/>
      <path d="M6 52 L30 74 L82 8" fill="none" stroke="var(--ink)" stroke-width="10" stroke-linejoin="miter"/>
    </svg>

    <section class="checklist">
      <div class="checklist__rail"></div>
      <div class="check-item check-item--mites">
        <div class="check-item__icon" role="img" aria-label="Illustration of an ear mite"></div>
        <p class="check-item__label">EAR<br>MITES</p>
      </div>
      <div class="check-item check-item--skin">
        <div class="check-item__icon" role="img" aria-label="Illustration of a sitting dog"></div>
        <p class="check-item__label">SKIN<br>HEALTH</p>
      </div>
      <div class="check-item check-item--fleas">
        <div class="check-item__icon" role="img" aria-label="Illustration of a tick"></div>
        <p class="check-item__label">FLEAS<br>&amp; TICKS</p>
      </div>
    </section>

    <footer class="footer">
      <p class="footer__label">SERVE BY:</p>
      <p class="footer__clinic">Meadowbrook Pet CLINIC</p>
    </footer>
  </main>
</body>
</html>
```